Facebook Design Project

We need a facebook design for my new edgy consulting business specializing in innovation, technology and strategy.

It is our personal goal to turn each client into raving fans by helping them achieve their own business goals and aspirations through assisting them in raising their own innovation and marketing standards.

We provide our personalised and state-of-the-art services to our clients and boards who represent some of the world greatest innovative thinkers.

Target Market(s)

Executives, Digital Directors, CFO, CEOs and Small Business

Industry/Entity Type

Marketing

Requirements
Must have
• Must Have:
- Please use some of the personal image(s) contained in the zip files which can be downloaded from here

http://vorbex.io/7K9P4T218M5D
http://vorbex.io/8f6r493H1k77
http://vorbex.io/5H8X6W4J9T3m

Nice to have
• Personable design

```html
<!DOCTYPE html>
<html lang="en">
<head>
<meta charset="utf-8">
<title>Callum Rourke Consultancy – Cover</title>
<link rel="stylesheet" href="https://fonts.googleapis.com/css2?family=Allura&family=Raleway:wght@400;500&display=swap">
<style>
  :root {
    --ink: #1c2a4c;
    --ink-soft: #2c3a5c;
    --sky: #dfe9f3;
    --sky-deep: #c9d8e8;
    --butter: #f7f4cf;
    --cream: #fbfbea;
    --band: rgba(255, 255, 255, 0.72);
    --portrait-light: #e8eef4;
    --portrait-mid: #a9b4c2;
    --portrait-dark: #7d8898;
  }

  html, body {
    margin: 0;
    padding: 0;
    overflow: hidden;
    background: #ffffff;
  }

  .cover {
    position: relative;
    width: 1200px;
    height: 445px;
    overflow: hidden;
    background:
      radial-gradient(ellipse 520px 260px at 260px 120px, var(--butter) 0%, rgba(247, 244, 207, 0) 100%),
      linear-gradient(180deg, var(--cream) 0%, #eef2ea 45%, var(--sky) 80%, var(--sky-deep) 100%);
  }

  .title-band {
    position: absolute;
    left: 0;
    top: 88px;
    width: 900px;
    height: 170px;
    background: linear-gradient(90deg, var(--band) 0%, var(--band) 80%, rgba(255, 255, 255, 0) 100%);
  }

  .brand {
    position: absolute;
    left: 170px;
    top: 96px;
    width: 745px;
    text-align: center;
    color: var(--ink);
  }

  .brand__name {
    margin: 0;
    font-family: "Allura", cursive;
    font-weight: 400;
    font-size: 82px;
    line-height: 94px;
    color: var(--ink);
  }

  .brand__rule {
    width: 392px;
    height: 1px;
    margin: 6px auto 12px;
    background: var(--ink-soft);
    border: 0;
  }

  .brand__kind {
    margin: 0;
    font-family: "Raleway", sans-serif;
    font-weight: 500;
    font-size: 31px;
    letter-spacing: 5px;
    line-height: 36px;
    color: var(--ink);
  }

  .brand__focus {
    margin: 18px 0 0;
    font-family: "Raleway", sans-serif;
    font-weight: 500;
    font-size: 17px;
    letter-spacing: 3.6px;
    line-height: 22px;
    color: var(--ink);
  }

  .portrait {
    position: absolute;
    right: 0;
    top: 0;
    width: 400px;
    height: 445px;
    background:
      radial-gradient(ellipse 150px 200px at 220px 420px, var(--portrait-dark) 0%, rgba(125, 136, 152, 0) 100%),
      radial-gradient(ellipse 80px 100px at 210px 120px, #d9bfae 0%, rgba(217, 191, 174, 0) 100%),
      linear-gradient(90deg, rgba(232, 238, 244, 0) 0%, var(--portrait-light) 25%, var(--portrait-mid) 60%, var(--portrait-light) 100%);
  }
</style>
</head>
<body>
  <main class="cover">
    <div class="title-band"></div>

    <div class="portrait" role="img" aria-label="Portrait photograph of the consultant in a light grey suit and tie, smiling, set against a bright window"></div>

    <header class="brand">
      <h1 class="brand__name">Callum Rourke</h1>
      <hr class="brand__rule">
      <p class="brand__kind">CONSULTANCY</p>
      <p class="brand__focus">INNOVATION, TECHNOLOGY AND STRATEGY</p>
    </header>
  </main>
</body>
</html>
```